BRANTWELL & BRANTWELL,LLP NEEDS A NEW LETTERHEAD DESIGN

a conservative yet contemporary layout befitting a long established
firm, consistent with the times, some form of logo so it catches ones attention, and is
admirable, but portrays integrity
Updates

I would like to approve #22066987 Please advise how to do this as it’s confusing on the site so I can approve payment for the designer

Target Market(s)

real estate investors and building management people

Industry/Entity Type

Law Firm

Font styles to use
Serif

Colors

Designer to choose colors to be used in the design.

Requirements
Must have
• some form of conservative logo

```html
<!DOCTYPE html>
<html lang="en">
<head>
<meta charset="utf-8">
<title>Brantwell &amp; Brantwell, LLP — Letterhead</title>
<link rel="stylesheet" href="https://fonts.googleapis.com/css2?family=Libre+Baskerville:wght@400&family=Arimo:wght@400&display=swap">
<style>
  :root {
    --backdrop: #e9eaec;
    --paper: #ffffff;
    --ink: #1f2326;
    --ink-soft: #3a3f44;
    --rule: #2b3035;
    --band: #2f3d47;
  }
  * { box-sizing: border-box; margin: 0; padding: 0; }
  html, body {
    width: 1200px;
    height: 795px;
    overflow: hidden;
    background: var(--backdrop);
  }
  .canvas {
    position: relative;
    width: 1200px;
    height: 795px;
  }
  .letterhead {
    position: absolute;
    left: 340px;
    top: 20px;
    width: 520px;
    height: 755px;
    background: var(--paper);
    box-shadow: 0 6px 22px rgba(0, 0, 0, 0.12);
  }
  .masthead {
    position: absolute;
    left: 44px;
    top: 44px;
    color: var(--ink);
  }
  .firm-name {
    font-family: "Libre Baskerville", "Times New Roman", serif;
    font-weight: 400;
    font-size: 16px;
    letter-spacing: 0;
    line-height: 1.2;
  }
  .firm-practice {
    margin-top: 5px;
    font-family: "Arimo", Arial, sans-serif;
    font-weight: 400;
    font-size: 8.4px;
    letter-spacing: 0.3px;
    line-height: 1.2;
    color: var(--ink-soft);
  }
  .contact-block {
    position: absolute;
    right: 36px;
    bottom: 40px;
    width: 380px;
    font-family: "Arimo", Arial, sans-serif;
    color: var(--ink-soft);
    text-align: right;
  }
  .contact-rule-top {
    margin-left: auto;
    width: 110px;
    height: 1.5px;
    background: var(--rule);
    margin-bottom: 7px;
  }
  .contact-line {
    font-size: 8.4px;
    line-height: 12px;
    white-space: nowrap;
  }
  .web-row {
    display: flex;
    align-items: center;
    gap: 8px;
    margin-top: 2px;
  }
  .web-row .rule {
    height: 1.5px;
    background: var(--rule);
  }
  .web-row .rule-left { flex: 1; }
  .web-row .rule-right { width: 16px; }
  .web-address {
    font-size: 8.4px;
    letter-spacing: 3px;
    white-space: nowrap;
  }
  .edge-band {
    position: absolute;
    left: 0;
    right: 0;
    bottom: 0;
    height: 9px;
    background: var(--band);
  }
</style>
</head>
<body>
<div class="canvas">
  <section class="letterhead">
    <header class="masthead">
      <div class="firm-name">Brantwell &amp; Brantwell, LLP</div>
      <div class="firm-practice">Property counsel for owners, managers and residents across New York</div>
    </header>

    <footer class="contact-block">
      <div class="contact-rule-top"></div>
      <p class="contact-line">48 Harbor Lane Suite 210, Brooklyn, New York 11299</p>
      <p class="contact-line">Phone: (555) 014-2287 | Fax: (555) 014-2290 | Email: info@brantwelllaw.com</p>
      <div class="web-row">
        <span class="rule rule-left"></span>
        <span class="web-address">www.brantwelllaw.com</span>
        <span class="rule rule-right"></span>
      </div>
    </footer>

    <div class="edge-band"></div>
  </section>
</div>
</body>
</html>
```